label update for bottle change

The goal is to adapt the label's design and shape to the new bottle, maintaining its defining elements such as the font, vertical name, company logo, background pattern, and color. The new design should not be identical to the old one, but rather an evolution of it. The gold stripe on the bottom is not mandatory, but the writing "VALLORIA DEL PIAVE / EST. 1892" must be retained, slightly enlarged.

The font name is: Brandon Text

```html
<!DOCTYPE html>
<html lang="it">
<head>
<meta charset="utf-8">
<title>Amaro di Carattere — Carciofo label</title>
<link rel="stylesheet" href="https://fonts.googleapis.com/css2?family=Montserrat:wght@600;700;800&display=swap">
<style>
  :root {
    --backdrop: #231f20;
    --label-green: #293d05;
    --gold: #a68a2a;
    --white: #ffffff;
  }
  html, body {
    margin: 0;
    padding: 0;
    width: 1200px;
    height: 1200px;
    overflow: hidden;
    background: var(--backdrop);
  }
  .label {
    position: absolute;
    left: 259px;
    top: 145px;
    width: 682px;
    height: 910px;
    box-shadow: 4px 6px 8px rgba(0,0,0,0.45);
  }
  .label svg { display: block; }
  .label text { font-family: "Montserrat", sans-serif; }
  .maker-line { font-weight: 700; font-size: 20px; fill: var(--white); }
  .maker-name { font-weight: 800; font-size: 32px; fill: var(--white); }
  .product-name { font-weight: 800; font-size: 116px; fill: var(--white); }
  .product-type { font-weight: 700; font-size: 40px; fill: var(--gold); }
  .origin { font-weight: 700; font-size: 18px; fill: var(--gold); }
  .founded { font-weight: 700; font-size: 18px; fill: var(--white); }
  .dot-gold { fill: var(--gold); }
  .dot-white { fill: var(--white); }
</style>
</head>
<body>
  <div class="label">
    <svg width="682" height="910" viewBox="0 0 682 910" xmlns="http://www.w3.org/2000/svg">
      <defs>
        <clipPath id="label-edge"><rect width="682" height="910"/></clipPath>
      </defs>
      <rect class="label-ground" width="682" height="910" fill="var(--label-green)"/>

      <g class="dot-pattern" clip-path="url(#label-edge)">
        <circle class="dot-white" cx="418" cy="248" r="34"/>
        <circle class="dot-gold" cx="592" cy="300" r="54"/>
        <circle class="dot-gold" cx="318" cy="452" r="22"/>
        <circle class="dot-white" cx="468" cy="548" r="72"/>
        <circle class="dot-gold" cx="668" cy="700" r="122"/>
        <circle class="dot-white" cx="326" cy="712" r="30"/>
        <circle class="dot-gold" cx="476" cy="836" r="42"/>
      </g>

      <g class="maker">
        <text class="maker-line" x="311" y="88" textLength="315" lengthAdjust="spacing">FABBRICA LIQUORI</text>
        <text class="maker-name" x="311" y="130" textLength="315" lengthAdjust="spacing">F.LLI CARAVELLI</text>
      </g>

      <text class="product-name" transform="translate(218 789) rotate(-90)" textLength="686" lengthAdjust="spacing">CARCIOFO</text>
      <text class="product-type" transform="translate(115 789) rotate(-90)" textLength="562" lengthAdjust="spacing">AMARO DI CARATTERE</text>

      <g class="provenance">
        <text class="origin" x="83" y="856" textLength="228" lengthAdjust="spacing">VALLORIA DEL PIAVE</text>
        <text class="founded" x="83" y="880" textLength="92" lengthAdjust="spacing">EST. 1892</text>
      </g>
    </svg>
  </div>
</body>
</html>
```